plumbing & gas fitting business card design

We need a business card design for a plumbing & gas fitting company. The company covers commercial, domestic and maintenance work. We would like a modern design communicating efficiency and sophistication. preferred colours would include (red grey & black) or (green grey & black). Please DO NOT include any water droplets.

Industry/Entity Type

Business

Contact Information for Business Card

Vortig Plumbing & Gas, Commercial Domestic & Maintenance, licence no. 617394K, ABN 47215830962, Phone 0417382956, Email vortigplumbingandgas@corvanet.com

```html
<!DOCTYPE html>
<html lang="en">
<head>
<meta charset="utf-8">
<title>Vortig Plumbing &amp; Gas — Business Card</title>
<link rel="stylesheet" href="https://fonts.googleapis.com/css2?family=Arimo:wght@400;700&display=swap">
<style>
  :root {
    --bg: #2b2b2b;
    --green: #7cb82a;
    --green-dark: #5f9a1c;
    --green-light: #9fd044;
    --grey: #555a5e;
    --ink: #2e3134;
    --card-white: #ffffff;
    --card-shade: #e4e6e7;
  }
  * { box-sizing: border-box; margin: 0; padding: 0; }
  html, body {
    width: 1200px; height: 901px; overflow: hidden;
    background: var(--bg);
    font-family: "Arimo", Arial, sans-serif;
  }
  .stage {
    position: relative; width: 1200px; height: 901px;
    display: flex; align-items: center; justify-content: center; gap: 40px;
  }
  .card {
    position: relative; width: 540px; height: 330px; overflow: hidden;
    box-shadow: 0 10px 30px rgba(0,0,0,0.45);
  }

  /* Back of card */
  .card-back {
    background: linear-gradient(135deg, var(--green-light) 0%, var(--green) 45%, var(--green-dark) 100%);
    display: flex; align-items: center; justify-content: center;
  }
  .card-back .gloss { position: absolute; inset: 0; width: 100%; height: 100%; }
  .card-back .brand {
    position: relative; display: flex; align-items: center; gap: 14px;
    color: var(--card-white); font-weight: 700; font-size: 34px; letter-spacing: 1px;
  }
  .brand .dot {
    width: 16px; height: 16px; border-radius: 50%; background: currentColor; flex: none;
  }

  /* Front of card */
  .card-front {
    background: linear-gradient(160deg, var(--card-white) 0%, var(--card-white) 40%, var(--card-shade) 100%);
  }
  .card-front .registration {
    position: absolute; top: 26px; right: 30px;
    font-size: 11px; line-height: 1.45; color: var(--ink);
  }
  .card-front .brand {
    position: absolute; top: 72px; left: 40px;
    display: flex; align-items: center; gap: 10px;
    color: var(--grey); font-weight: 700; font-size: 27px; letter-spacing: 0.5px;
  }
  .card-front .brand .dot { width: 12px; height: 12px; background: var(--green); }
  .contact { position: absolute; left: 40px; top: 150px; color: var(--ink); }
  .contact .name {
    color: var(--green); font-size: 19px; letter-spacing: 0.5px; text-transform: uppercase;
  }
  .contact .role { font-size: 13px; font-weight: 700; margin-top: 2px; }
  .contact .lines { margin-top: 18px; font-size: 15px; line-height: 1.35; }
  .contact .lines b { color: var(--green); font-weight: 700; display: inline-block; width: 14px; }
  .services-band {
    position: absolute; left: 0; right: 0; bottom: 0; height: 62px;
    background: var(--green);
    display: flex; align-items: center; justify-content: flex-end; padding-right: 34px;
    color: var(--card-white); font-size: 20px; letter-spacing: 0.5px;
  }
</style>
</head>
<body>
  <main class="stage">
    <section class="card card-back" aria-label="Card back">
      <svg class="gloss" viewBox="0 0 540 330" preserveAspectRatio="none" aria-hidden="true">
        <path d="M0 0 H330 Q250 170 0 260 Z" fill="#ffffff" fill-opacity="0.10"/>
      </svg>
      <div class="brand"><span class="dot"></span>Vortig Plumbing &amp; Gas</div>
    </section>

    <section class="card card-front" aria-label="Card front">
      <div class="registration">
        Licence no. 617394K<br>
        ABN 47215830962
      </div>
      <div class="brand"><span class="dot"></span>Vortig Plumbing &amp; Gas</div>
      <div class="contact">
        <p class="name">Dario Vortig</p>
        <p class="role">Director</p>
        <p class="lines">
          <b>P</b> 0417 382 956<br>
          <b>E</b> vortigplumbingandgas@corvanet.com
        </p>
      </div>
      <div class="services-band">Commercial Domestic &amp; Maintenance</div>
    </section>
  </main>
</body>
</html>
```